Real Estate Investing company needs a business card design

We need a business card design for new Real Estate Investment Company called "Maple Ridge Ventures, LLC." We buy homes for cash and close quickly in any situation. Our company provides an easy and fast option for home owners who are in tough situations who need to sell their home fast and don't want realtor fees or other listing hassles. We also renovate and resell our homes which helps provide housing for the community. We would like to see designs that use the colors blue and white to match our company logo or other colors that may match our company logo. The final design should communicate trust and easy process.
Industry/Entity Type
Business
Contact Information for Business Card
Front should have company name and company logo. back of card should have company logo and area to list services.
Look and feel

```html
<!DOCTYPE html>
<html lang="en">
<head>
<meta charset="utf-8">
<title>Maple Ridge Ventures, LLC — Business Card</title>
<link rel="stylesheet" href="https://fonts.googleapis.com/css2?family=Open+Sans:wght@400;700&display=swap">
<style>
  :root {
    --backdrop: #e5e5e5;
    --paper: #ffffff;
    --brand-blue: #1572b8;
    --mid-blue: #0f64aa;
    --deep-blue: #0b5c9e;
    --icon-blue: #1f7cc2;
    --ink-white: #ffffff;
  }
  * { box-sizing: border-box; margin: 0; padding: 0; }
  html, body {
    width: 1200px; height: 1200px; overflow: hidden;
    background: var(--backdrop);
    font-family: "Open Sans", Arial, sans-serif;
  }
  .card {
    position: absolute; left: 257px;
    width: 689px; height: 394px;
    background: var(--paper); overflow: hidden;
  }
  .card--front { top: 174px; }
  .card--back { top: 618px; }
  .card__art { position: absolute; inset: 0; width: 100%; height: 100%; }
  .brand {
    position: absolute; left: 0; right: 0;
    display: flex; align-items: center; justify-content: center; gap: 12px;
    color: var(--brand-blue); font-weight: 700; white-space: nowrap;
  }
  .brand__mark { background: var(--brand-blue); flex: none; }
  .card--front .brand { top: 178px; font-size: 34px; }
  .card--front .brand__mark { width: 26px; height: 26px; }
  .card--back .brand { top: 98px; font-size: 28px; }
  .card--back .brand__mark { width: 22px; height: 22px; }
  .holder {
    position: absolute; left: 18px; width: 195px; top: 277px;
    color: var(--ink-white); text-align: center;
  }
  .holder__name { font-size: 32px; line-height: 36px; padding-bottom: 4px; border-bottom: 2px solid var(--ink-white); }
  .holder__role { font-size: 27px; line-height: 36px; margin-top: 2px; }
  .contact { position: absolute; color: var(--ink-white); font-size: 16px; line-height: 22px; white-space: nowrap; }
</style>
</head>
<body>
  <section class="card card--front">
    <svg class="card__art" viewBox="0 0 689 394" aria-hidden="true">
      <polygon points="144,0 689,0 689,34 134,34" fill="var(--brand-blue)"/>
      <rect x="0" y="352" width="689" height="42" fill="var(--brand-blue)"/>
    </svg>
    <div class="brand"><span class="brand__mark"></span>Maple Ridge Ventures, LLC</div>
  </section>

  <section class="card card--back">
    <svg class="card__art" viewBox="0 0 689 394" aria-hidden="true">
      <polygon points="144,0 689,0 689,34 134,34" fill="var(--brand-blue)"/>
      <polygon points="0,236 224,236 244,394 0,394" fill="var(--brand-blue)"/>
      <polygon points="218,229 293,223 318,394 244,394" fill="var(--mid-blue)"/>
      <polygon points="293,223 298,223 324,394 318,394" fill="var(--paper)"/>
      <polygon points="298,223 689,223 689,394 324,394" fill="var(--deep-blue)"/>
      <g class="icons" fill="none" stroke="var(--ink-white)" stroke-width="1.4">
        <circle cx="273" cy="246" r="11" fill="var(--icon-blue)" stroke="none"/>
        <path d="M266 243 q7 -5 14 0 l0 2.5 l-3 1 l-1 -2 q-3 -1 -6 0 l-1 2 l-3 -1 z" fill="var(--ink-white)" stroke="none"/>
        <path d="M269.5 247 h7 l2.5 5 h-12 z" fill="var(--ink-white)" stroke="none"/>
        <circle cx="279" cy="279" r="11" fill="var(--icon-blue)" stroke="none"/>
        <rect x="273" y="275" width="12" height="8"/>
        <path d="M273 275 l6 5 l6 -5"/>
        <circle cx="286" cy="319" r="11" fill="var(--icon-blue)" stroke="none"/>
        <path d="M286 326 q-5 -6 -5 -9 a5 5 0 0 1 10 0 q0 3 -5 9 z" fill="var(--ink-white)" stroke="none"/>
        <circle cx="292" cy="352" r="11" fill="var(--icon-blue)" stroke="none"/>
        <circle cx="292" cy="352" r="6"/>
        <path d="M286 352 h12 M292 346 q-4 6 0 12 q4 -6 0 -12"/>
      </g>
    </svg>
    <div class="brand"><span class="brand__mark"></span>Maple Ridge Ventures, LLC</div>
    <div class="holder">
      <p class="holder__name">NAME</p>
      <p class="holder__role">POSITION</p>
    </div>
    <p class="contact" style="left:322px; top:235px;">+63 555 010 2040</p>
    <p class="contact" style="left:329px; top:268px;">hello@mapleridgeventures.com</p>
    <p class="contact" style="left:333px; top:308px;">Unit 8, 42 Cedar Ln, Manila, Philippines</p>
    <p class="contact" style="left:333px; top:341px;">www.mapleridgeventures.com</p>
  </section>
</body>
</html>
```